Business Card Design/Stationary Design

We would like designers to submit cool, hip business card designs (plus stationary designs) for a new, upstart software development company located in Toronto.
If you have any questions, please email us.
For inspiration on designs:
http://cardmuse.example/cool-business-cards/
http://layoutnotes.example/2008/05/36-cool-business-cards-you-should%E2%80%99ve-seen.html
http://gigharbor.example/general/18-smokin-hot-business-card-designs/

Card info:

Selvakumar (Selv) Nadarasan

Founder and CEO

47 Brindle Court, Suite 311

Toronto, ON M4K 2T8

Phone: 647-512-7730

Mobile: 416-273-5094

Fax: 647-512-7731

Email: selvakumar.nadarasan@mailbrook.example

www.quendrix.example
Updates

Hi everyone,

In terms of all the designs I have seen so far, here is what I like:

1.  I really like the "back" part of this design.  The "front" looks pretty decent as well, but for the "front", look at #2 on this list.  I like that.

http://www.pitchboard.example/image.aspx?imageLocation=1000_10001_2000_image.jpg&type=design300px&whiteLabelCustId=9999

2. "Side 1" of this I like, the front needs to be reworked.

http://www.pitchboard.example/image.aspx?imageLocation=1000_10002_2000_image.png&type=design300px&whiteLabelCustId=9999

3. http://www.pitchboard.example/image.aspx?imageLocation=1000_10003_2000_image.jpg&type=design300px&whiteLabelCustId=9999

4. http://www.pitchboard.example/image.aspx?imageLocation=1000_10004_2000_image.jpg&type=design300px&whiteLabelCustId=9999

Target Market(s)

We are focused on enterprise customers right now, so businesses with a long-term goal of also reaching out to the consumer market as well.

Industry/Entity Type

Software

Requirements
Must have
• Must look cool, ultra-modern, clean and eye-catching. Must incorporate our logo and the colors found in the logo.

```html
<!DOCTYPE html>
<html lang="en">
<head>
<meta charset="utf-8">
<title>Quendrix Stationery</title>
<link rel="stylesheet" href="https://fonts.googleapis.com/css2?family=Questrial&family=Source+Sans+3:wght@400;600&display=swap">
<style>
  :root {
    --ink: #111111;
    --leaf: #4e8f03;
    --lime: #78d400;
    --chartreuse: #c7f000;
    --url-green: #4c8c0a;
    --mist: #c9cfc4;
    --paper: #ffffff;
  }
  * { margin: 0; padding: 0; box-sizing: border-box; }
  html, body { width: 1173px; height: 1200px; overflow: hidden; background: var(--paper); }
  body { position: relative; font-family: "Source Sans 3", sans-serif; color: var(--ink); }

  /* Letterhead */
  .letterhead {
    position: absolute; left: 312px; top: 1px; width: 860px; height: 1121px;
    border: 1.5px solid var(--ink); background: var(--paper); overflow: hidden;
  }
  .brand { position: absolute; display: flex; align-items: center; font-family: "Questrial", sans-serif; color: var(--ink); }
  .brand__dot { border-radius: 50%; background: var(--lime); flex: none; }
  .letterhead .brand { left: 36px; top: 48px; gap: 28px; }
  .letterhead .brand__dot { width: 116px; height: 116px; }
  .letterhead .brand__name { font-size: 74px; line-height: 1; }

  .sender { position: absolute; right: 34px; top: 26px; font-family: "Questrial", sans-serif; font-size: 15px; line-height: 17.5px; text-align: right; }
  .sender__lines { margin-bottom: 10px; }
  .sender__contacts { display: grid; grid-template-columns: auto auto; column-gap: 8px; }
  .sender__label { font-size: 12.5px; }

  .letterhead__wave { position: absolute; left: 0; top: 158px; width: 860px; height: 72px; }

  .recipient { position: absolute; right: 70px; top: 242px; font-size: 17.5px; }

  .letter { position: absolute; left: 62px; top: 294px; width: 732px; font-size: 17.6px; line-height: 23.1px; }
  .letter__aside { padding-left: 58px; }
  .letter__aside--open { margin-bottom: 46px; }
  .letter p { text-align: justify; text-indent: 58px; margin-bottom: 23px; hyphens: auto; }
  .letter .letter__aside { text-indent: 0; text-align: left; }

  .letterhead__url { position: absolute; left: 14px; width: 860px; top: 1080px; text-align: center; font-family: "Questrial", sans-serif; font-weight: 700; font-size: 25px; letter-spacing: 2px; color: var(--url-green); }
  .letterhead .brand--faint { left: 688px; top: 1060px; gap: 10px; color: var(--mist); }
  .brand--faint .brand__dot { width: 36px; height: 36px; background: #dcefc0; }
  .brand--faint .brand__name { font-size: 25px; }

  /* Business card */
  .card {
    position: absolute; left: 1px; top: 742px; width: 277px; height: 485px;
    transform-origin: 0 0; transform: rotate(-20deg);
    border: 1.5px solid var(--ink); background: var(--paper); overflow: hidden;
  }
  .card__field { position: absolute; left: 0; top: 0; width: 277px; height: 485px; }
  .card .brand { left: 14px; top: 50px; gap: 12px; }
  .card .brand__dot { width: 60px; height: 60px; }
  .card .brand__name { font-size: 44px; line-height: 1; }
  .card__role { position: absolute; left: 17px; top: 176px; font-size: 9px; color: var(--chartreuse); }
  .card__name { position: absolute; left: 26px; top: 190px; font-family: "Questrial", sans-serif; font-size: 22px; color: var(--paper); white-space: nowrap; }
  .card__details { position: absolute; left: 0; width: 277px; text-align: center; font-family: "Questrial", sans-serif; color: var(--paper); }
  .card__address { top: 242px; font-size: 15.5px; line-height: 19px; }
  .card__phones { top: 334px; font-size: 15.5px; line-height: 19px; }
  .card__email { top: 410px; font-size: 11px; }
  .card__url { position: absolute; left: 0; width: 277px; top: 448px; text-align: center; font-family: "Questrial", sans-serif; font-weight: 700; font-size: 24px; letter-spacing: 1.5px; color: var(--chartreuse); }
</style>
</head>
<body>

<section class="letterhead">
  <div class="brand">
    <span class="brand__dot"></span>
    <span class="brand__name">Quendrix</span>
  </div>

  <address class="sender" style="font-style: normal;">
    <div class="sender__lines">47 Brindle Court<br>Suite 311<br>Toronto, ON<br>M4K 2T8</div>
    <div class="sender__contacts">
      <span class="sender__label">office:</span><span>(647) 512-7730</span>
      <span class="sender__label">fax:</span><span>(647) 512-7731</span>
      <span class="sender__label">mobile:</span><span>(416) 273-5094</span>
    </div>
  </address>

  <svg class="letterhead__wave" viewBox="0 0 860 72" aria-hidden="true">
    <path fill="var(--chartreuse)" d="M0 30 C200 -12 420 -4 580 26 C700 46 800 40 860 16 L860 36 C800 58 700 62 580 44 C420 16 200 14 0 52 Z"/>
    <path fill="var(--lime)" d="M0 48 C200 10 420 12 580 40 C700 58 800 52 860 28 L860 46 C800 66 700 68 580 56 C420 30 200 28 0 70 Z"/>
  </svg>

  <div class="recipient">Ladata Gosea Haream</div>

  <div class="letter">
    <div class="letter__aside letter__aside--open">Aliquam vitae diam lorem.<br>Vestibulum rutrum aliquam volutpat.</div>
    <p>Lorem ipsum dolor sit amet, consectetur adipiscing elit. Phasellus in adipiscing diam. Proin vehicula facilisis sodales. Fusce rhoncus euismod leo, vel aliquet massa accumsan eu. Quisque luctus, leo et mollis suscipit, justo lectus lobortis risus, laoreet tincidunt risus velit et augue. Sed sollicitudin justo id ligula mattis in tempor dui pharetra.</p>
    <p>Cras volutpat pulvinar urna, et volutpat turpis consequat ut. Morbi at placerat nibh. Fusce nec urna nec sem rhoncus vestibulum. Aenean blandit dignissim scelerisque. Duis vel diam eu erat consequat blandit. Praesent iaculis interdum libero eu placerat. Vivamus nec nunc augue. Nullam ut blandit neque. Mauris lobortis, turpis ac lobortis fringilla, augue ligula scelerisque turpis, a tempus ante dolor at justo. In vitae orci vitae tortor blandit euismod. Morbi in volutpat nibh.</p>
    <p>Maecenas faucibus odio ac augue scelerisque eu elementum tortor pellentesque. Integer ut dui in metus pharetra placerat et sed tellus. Nulla neque tellus, laoreet vitae adipiscing ac, auctor at nulla. Ut tempor, sem quis aliquet consequat, est ligula volutpat dolor, ullamcorper lacinia magna augue id eros. Lorem ipsum dolor sit amet, consectetur adipiscing elit.</p>
    <p>Vivamus accumsan accumsan placerat. Integer eu ligula sit amet ipsum placerat facilisis sed vitae tortor. Nullam sit amet dolor commodo lorem malesuada tempor a id sapien. Sed in tortor ut ante mollis ultricies vel eu diam. Nulla id pretium orci. Ut accumsan posuere quam, at tincidunt dui hendrerit id.</p>
    <div class="letter__aside">Aliquam vitae diam lorem.<br>Vestibulum rutrum aliquam volutpat.</div>
  </div>

  <div class="letterhead__url">www.quendrix.example</div>

  <div class="brand brand--faint">
    <span class="brand__dot"></span>
    <span class="brand__name">Quendrix</span>
  </div>
</section>

<section class="card">
  <svg class="card__field" viewBox="0 0 277 485" aria-hidden="true">
    <path fill="var(--chartreuse)" d="M0 150 C40 105 110 92 170 86 C220 80 255 66 277 48 L277 485 L0 485 Z"/>
    <path fill="var(--lime)" d="M0 160 C40 115 110 100 170 94 C220 88 255 74 277 56 L277 485 L0 485 Z"/>
    <path fill="var(--leaf)" d="M0 172 C40 126 110 110 170 104 C220 98 255 84 277 66 L277 485 L0 485 Z"/>
  </svg>

  <div class="brand">
    <span class="brand__dot"></span>
    <span class="brand__name">Quendrix</span>
  </div>

  <div class="card__role">Founder &amp; CEO</div>
  <div class="card__name">Selvakumar Nadarasan</div>

  <div class="card__details card__address">47 Brindle Court<br>Suite 311<br>Toronto, ON<br>M4K 2T8</div>
  <div class="card__details card__phones">(647) 512-7730<br>(647) 512-7731<br>(416) 273-5094</div>
  <div class="card__details card__email">selvakumar.nadarasan@mailbrook.example</div>
  <div class="card__url">www.quendrix.example</div>
</section>

</body>
</html>
```